Label design needed for cafe display

Hi,
We need a label designed so that we can label food in our display fridge.
The label would have to be editable, as we have lot's of different food items.. and we change the items often, so I would be constantly updating the labels. I will then be printing each label, and laminating them, then displaying them in our food display fridge.
We would like the label to contain our logo - which I have attached.
I have also attached our menus, so you can get a feel for the designs we like.
An example of what we need on a label:
QUICHE LORRAINE $7.50
With Salad $9.50
Please feel free to ask me any questions.
Printing

```html
<!DOCTYPE html>
<html lang="en">
<head>
<meta charset="utf-8">
<title>Fridge Display Labels</title>
<link rel="stylesheet" href="https://fonts.googleapis.com/css2?family=Courier+Prime:wght@400;700&display=swap">
<style>
  :root {
    --backdrop: #2d2b2b;
    --label-cream: #fbf5a0;
    --brand-brown: #3e3230;
    --panel-white: #ffffff;
    --ink-dark: #3e3230;
    --ink-light: #ffffff;
    --ink-cream: #fbf5a0;
  }
  * { margin: 0; padding: 0; box-sizing: border-box; }
  html, body {
    width: 1200px;
    height: 680px;
    overflow: hidden;
    background: var(--backdrop);
  }
  .canvas {
    position: relative;
    width: 1200px;
    height: 680px;
  }
  .label {
    position: absolute;
    left: 0;
    width: 1200px;
    height: 190px;
  }
  .label--light { top: 110px; }
  .label--dark  { top: 368px; }
  .label__shape {
    position: absolute;
    inset: 0;
    filter: drop-shadow(2px 3px 3px rgba(0,0,0,0.55));
  }
  .brand {
    position: absolute;
    left: 135px;
    top: 18px;
    width: 150px;
    height: 150px;
    border-radius: 50%;
    background: var(--brand-brown);
    display: flex;
    flex-direction: column;
    align-items: center;
    justify-content: center;
    font-family: "Courier Prime", monospace;
    font-weight: 400;
    font-size: 19px;
    line-height: 1.15;
    letter-spacing: 2px;
    color: #d9d2cf;
    text-align: center;
  }
  .menu-item {
    position: absolute;
    right: 190px;
    top: 22px;
    text-align: right;
    font-family: "Courier Prime", monospace;
    font-weight: 700;
    font-size: 54px;
    line-height: 66px;
    letter-spacing: -0.5px;
  }
  .label--light .menu-item__name,
  .label--light .menu-item__option { color: var(--ink-dark); }
  .label--dark .menu-item__name { color: var(--ink-cream); }
  .label--dark .menu-item__option { color: var(--ink-light); }
</style>
</head>
<body>
<main class="canvas">

  <section class="label label--light">
    <svg class="label__shape" width="1200" height="190" viewBox="0 0 1200 190" aria-hidden="true">
      <polygon points="120,8 1075,8 1037,95 1075,180 120,180" fill="var(--label-cream)"/>
      <polygon points="298,20 1058,20 1020,95 1058,168 298,168" fill="var(--panel-white)" stroke="#3e3230" stroke-width="1"/>
    </svg>
    <div class="brand">HOUSE<br>CALL</div>
    <div class="menu-item">
      <p class="menu-item__name">QUICHE LORRAINE $7.50</p>
      <p class="menu-item__option">With Salad $9.50</p>
    </div>
  </section>

  <section class="label label--dark">
    <svg class="label__shape" width="1200" height="190" viewBox="0 0 1200 190" aria-hidden="true">
      <polygon points="120,8 1075,8 1037,95 1075,180 120,180" fill="var(--label-cream)"/>
      <polygon points="298,20 1058,20 1020,95 1058,168 298,168" fill="var(--brand-brown)"/>
    </svg>
    <div class="brand">HOUSE<br>CALL</div>
    <div class="menu-item">
      <p class="menu-item__name">QUICHE LORRAINE $7.50</p>
      <p class="menu-item__option">With Salad $9.50</p>
    </div>
  </section>

</main>
</body>
</html>
```